New Business Card Design Project VORALDI-Italy

we are VORALDI-Italy
our company in the market for 3 years we are luxury cosmetic company and its about time for a facelift :)
i will like to have elegant luxurious and unique business card
that will give the person that get it a unique, luxurious and elegant impression
I'm VERY OPEN FOR NEW IDEAS , even duo i add a few files of things that i see on line and i like them

i add my logo as well
my website is VORALDI.COM
(if you would like to see the main style that we have)

Target Market(s)

adult that have money :)

Industry/Entity Type

Business

Contact Information for Business Card

Name - Paul Voraldi
Position - CEO and CO Founder
address - 4718 E Danbury
telephone - 555-318-4402
email - paul@voraldi-example.com
fax - 555-318-4402
website - VORALDI.COM

Colors
000000
959595
fbee3e
ffffff

Requirements
Must have
• big logo in GOLD color
• elegant look
• impressive
Nice to have
• not must but maybe classy pattern background
• not must but maybe emblem
• maybe clear plastic business card
Should not have
• colors
• images

```html
<!DOCTYPE html>
<html lang="en">
<head>
<meta charset="utf-8">
<title>VORALDI-Italy Business Card</title>
<link href="https://fonts.googleapis.com/css2?family=Crimson+Text:wght@400;600&display=swap" rel="stylesheet">
<style>
  :root {
    --page-bg: #e9e5e0;
    --gold: #c9a24a;
    --gold-deep: #a97f2c;
    --ink: #0b0b0b;
    --ink-soft: #2a2a2a;
    --silver: #e2e2e2;
    --frost-light: #f4f2f0;
    --frost-mid: #dcdad8;
    --frost-blush: #e8cfd2;
  }
  html, body {
    margin: 0;
    padding: 0;
    width: 1200px;
    height: 970px;
    overflow: hidden;
    background: var(--page-bg);
    font-family: "Crimson Text", Georgia, serif;
  }
  .business-card {
    position: absolute;
    left: 150px;
    top: 228px;
    width: 900px;
    height: 514px;
    border-radius: 22px;
    overflow: hidden;
    box-shadow: 0 18px 40px rgba(0,0,0,0.18);
  }
  .card-front {
    position: absolute;
    left: 0; top: 0;
    width: 485px;
    height: 100%;
    background:
      radial-gradient(ellipse at 55% 72%, var(--frost-blush) 0%, rgba(232,207,210,0) 45%),
      linear-gradient(160deg, var(--frost-light) 0%, var(--frost-mid) 100%);
  }
  .card-back {
    position: absolute;
    left: 489px; top: 0;
    right: 0;
    height: 100%;
    background: linear-gradient(135deg, var(--ink) 0%, var(--ink-soft) 100%);
  }
  .gold-divider {
    position: absolute;
    left: 485px; top: 0;
    width: 4px;
    height: 100%;
    background: linear-gradient(180deg, var(--gold) 0%, var(--gold-deep) 100%);
  }
  .brand-mark {
    position: absolute;
    left: 0; width: 485px;
    top: 110px;
    text-align: center;
  }
  .brand-mark .mark-circle {
    display: block;
    margin: 0 auto 50px;
    width: 140px;
    height: 140px;
  }
  .brand-name {
    font-size: 62px;
    font-weight: 400;
    color: var(--gold);
    letter-spacing: 1px;
    line-height: 1;
  }
  .contact-block {
    position: absolute;
    left: 558px;
    top: 98px;
    color: var(--silver);
  }
  .person-name {
    font-size: 32px;
    font-weight: 600;
    color: var(--gold);
    line-height: 1;
    margin: 0;
  }
  .person-role {
    font-size: 22px;
    margin: 6px 0 0;
    line-height: 1.1;
  }
  .company-name {
    font-size: 23px;
    font-weight: 600;
    color: var(--gold);
    margin: 32px 0 0;
    line-height: 1.1;
  }
  .company-address {
    font-size: 22px;
    margin: 6px 0 0;
    line-height: 1.1;
  }
  .contact-list {
    list-style: none;
    margin: 34px 0 0;
    padding: 0;
  }
  .contact-list li {
    display: flex;
    align-items: center;
    font-size: 22px;
    line-height: 33px;
  }
  .contact-list svg {
    width: 20px;
    height: 20px;
    margin-right: 12px;
    fill: none;
    stroke: var(--gold);
    stroke-width: 1.8;
  }
  .contact-list .filled { fill: var(--gold); stroke: none; }
</style>
</head>
<body>
  <div class="business-card">
    <div class="card-front">
      <div class="brand-mark">
        <svg class="mark-circle" viewBox="0 0 140 140" aria-hidden="true">
          <circle cx="70" cy="70" r="66" fill="none" stroke="#c9a24a" stroke-width="4"/>
        </svg>
        <div class="brand-name">VORALDI</div>
      </div>
    </div>
    <div class="gold-divider"></div>
    <div class="card-back"></div>

    <div class="contact-block">
      <p class="person-name">Paul Voraldi</p>
      <p class="person-role">CEO and CO Founder</p>
      <p class="company-name">VORALDI-Italy</p>
      <p class="company-address">4718 E Danbury</p>
      <ul class="contact-list">
        <li>
          <svg viewBox="0 0 24 24" aria-label="Phone"><path class="filled" d="M6.6 10.8c1.4 2.8 3.8 5.1 6.6 6.6l2.2-2.2c.3-.3.7-.4 1-.2 1.1.4 2.3.6 3.6.6.6 0 1 .4 1 1V20c0 .6-.4 1-1 1C10.6 21 3 13.4 3 4c0-.6.4-1 1-1h3.5c.6 0 1 .4 1 1 0 1.3.2 2.5.6 3.6.1.3 0 .7-.2 1z"/></svg>
          555-318-4402
        </li>
        <li>
          <svg viewBox="0 0 24 24" aria-label="Fax"><path class="filled" d="M7 3h10v5H7zM4 9h16a1 1 0 0 1 1 1v7h-4v4H7v-4H3v-7a1 1 0 0 1 1-1zm5 7v3h6v-3z"/></svg>
          555-318-4402
        </li>
        <li>
          <svg viewBox="0 0 24 24" aria-label="Email"><path class="filled" d="M3 6h18v12H3zM4.5 7.5 12 13l7.5-5.5z"/></svg>
          paul@voraldi-example.com
        </li>
        <li>
          <svg viewBox="0 0 24 24" aria-label="Website"><circle cx="12" cy="12" r="9"/><ellipse cx="12" cy="12" rx="4" ry="9"/><path d="M3 12h18M5 7h14M5 17h14"/></svg>
          VORALDI.COM
        </li>
      </ul>
    </div>
  </div>
</body>
</html>
```